Brim Contractors

We are a group of people that doing a picking fruits like Oranges and grapes seasonal. We would like to have the colors " light black or black " back ground of the card. Thanks

Industry/Entity Type

Group

Contact Information for Business Card

Mob 0472915364 . Fax 03 5187 3942. P.O.Box 517 Darnvale Vic 3581

```html
<!DOCTYPE html>
<html lang="en">
<head>
<meta charset="utf-8">
<title>Brim Contractors – Business Card</title>
<link rel="stylesheet" href="https://fonts.googleapis.com/css2?family=Ubuntu:wght@700&display=swap">
<style>
  :root {
    --backdrop: #2a211c;
    --card: #050505;
    --gold: #dc9a2c;
    --ember: #d8541f;
    --fruit-orange: #c4531f;
    --fruit-gold: #b98428;
  }
  * { margin: 0; padding: 0; box-sizing: border-box; }
  html, body { width: 1200px; height: 900px; overflow: hidden; }
  body {
    background: var(--backdrop);
    font-family: "Ubuntu", Arial, sans-serif;
    font-weight: 700;
  }
  .business-card {
    position: absolute;
    left: 100px; top: 165px;
    width: 1000px; height: 570px;
    background: var(--card);
    border-radius: 36px;
    box-shadow: 0 20px 50px rgba(0,0,0,.55);
  }
  .brand-name {
    position: absolute;
    left: 95px; top: 205px;
    font-size: 68px;
    color: var(--gold);
    letter-spacing: 1px;
  }
  .fruit-art {
    position: absolute;
    border-radius: 50%;
  }
  .fruit-art--orange {
    left: 770px; top: 40px; width: 150px; height: 150px;
    background: radial-gradient(circle at 45% 45%, #3a1a0c 0%, var(--fruit-orange) 90%);
  }
  .fruit-art--grape {
    left: 640px; top: 210px; width: 190px; height: 170px;
    background: radial-gradient(circle at 50% 45%, #2e2110 0%, var(--fruit-gold) 95%);
  }
  .contact-list {
    position: absolute;
    left: 120px; top: 380px;
    padding-left: 28px;
    border-left: 4px solid var(--ember);
    height: 130px;
    display: flex; flex-direction: column; justify-content: center; gap: 12px;
  }
  .contact-item {
    display: flex; align-items: center; gap: 16px;
    font-size: 30px;
    color: var(--gold);
    letter-spacing: 1px;
  }
  .contact-icon { width: 24px; height: 26px; flex: none; }
  .address-rule {
    position: absolute;
    left: 545px; top: 420px;
    width: 420px; height: 3px;
    background: var(--ember);
  }
  .postal-address {
    position: absolute;
    right: 40px; top: 440px;
    font-size: 26px;
    color: var(--gold);
    letter-spacing: 1px;
  }
</style>
</head>
<body>
  <main class="business-card">
    <div class="fruit-art fruit-art--orange" role="img" aria-label="Illustration of a cartoon orange slice"></div>
    <div class="fruit-art fruit-art--grape" role="img" aria-label="Illustration of a cartoon round fruit"></div>

    <h1 class="brand-name">Brim Contractors</h1>

    <ul class="contact-list">
      <li class="contact-item">
        <svg class="contact-icon" viewBox="0 0 24 26" aria-hidden="true">
          <rect x="6" y="2" width="12" height="22" rx="2" fill="none" stroke="var(--ember)" stroke-width="2"/>
          <line x1="10" y1="20" x2="14" y2="20" stroke="var(--ember)" stroke-width="2"/>
        </svg>
        <span>0472915364</span>
      </li>
      <li class="contact-item">
        <svg class="contact-icon" viewBox="0 0 24 26" aria-hidden="true">
          <rect x="6" y="2" width="12" height="8" fill="none" stroke="var(--ember)" stroke-width="2"/>
          <rect x="2" y="10" width="20" height="13" rx="2" fill="var(--ember)"/>
          <line x1="6" y1="16" x2="18" y2="16" stroke="var(--card)" stroke-width="2"/>
        </svg>
        <span>03 5187 3942</span>
      </li>
    </ul>

    <div class="address-rule"></div>
    <p class="postal-address">P.O.Box 517 Darnvale Vic 3581</p>
  </main>
</body>
</html>
```